Enhance existing websites

Hello,

With my very limited web design knowledge I have designed my own websites...
Trailquote.example
Rovervalue.example

Whilst I have been very happy with the response I have received I feel the sites need enhancing. Here is what I would like to change..

1, Place a shadow around the whole pages outline so it has a 3d effect with a better background colour.

2, Improve the 'Request a valuation' tab so it stands out, maybe to also insert a curved arrow(s) to direct customer to click 'request a valuation' . Naturally this would need to be done on each page.

3, The testimonials of the 'what customers say' to change every few seconds.

4, The front page image to change every few seconds to a image of my choice.

5, any other suggestions you feel would benefit my site (obviously willing to pay extra for this and within this site)

6, given my limited knowledge my html code will surely need tidying also

7, if possible any changes not to affect my very good google ratings.

Price paid is for both sites as they're practically identical.

Thanks in advance

Glen

```html
<!DOCTYPE html>
<html lang="en">
<head>
<meta charset="utf-8">
<title>Trailquote.example – Sell your caravan</title>
<link href="https://fonts.googleapis.com/css2?family=PT+Sans:wght@400;700&display=swap" rel="stylesheet">
<style>
:root{
  --orange:#e8922a;
  --orange-dark:#d27d18;
  --blue:#4a85c0;
  --blue-dark:#3a6fa6;
  --navy:#1d2633;
  --bg-top:#3d4d66;
  --bg-bottom:#2a3a52;
  --text:#333a44;
  --muted:#6a6f77;
  --line:#e4e4e4;
  --light:#f3f3f3;
  --white:#ffffff;
}
*{box-sizing:border-box;margin:0;padding:0}
html,body{width:1200px;height:2239px;overflow:hidden}
body{font-family:"PT Sans",Arial,sans-serif;color:var(--text);background:linear-gradient(180deg,var(--bg-top) 0,#2f3f58 500px,var(--bg-bottom) 100%);position:relative}
.city-backdrop{position:absolute;left:0;top:0;width:1200px;height:520px;background:linear-gradient(180deg,#5a6a82 0,#46566f 55%,rgba(42,58,82,0) 100%)}
.abs{position:absolute}
.page-shadow{position:absolute;left:104px;top:64px;width:996px;height:2112px;background:#e9e9e9;box-shadow:0 0 28px rgba(0,0,0,.55)}
.page{position:absolute;left:113px;top:72px;width:977px;height:2029px;background:var(--white);overflow:hidden}

/* header */
.logo{left:62px;top:30px}
.logo-name{font-size:29px;font-weight:700;color:var(--blue);letter-spacing:.3px;line-height:1}
.logo-tag{font-size:11.5px;font-weight:700;color:var(--text);margin-top:3px}
.nav{left:384px;top:52px;display:flex;font-size:14px}
.nav a{color:var(--text);text-decoration:none;margin-right:37px}
.nav a.active{color:var(--orange)}
.btn{display:flex;align-items:center;justify-content:center;color:#fff;font-size:13.5px;font-weight:700;text-transform:uppercase;border-radius:2px}
.btn-join{left:733px;top:38px;width:96px;height:36px;background:var(--orange)}
.btn-login{left:839px;top:38px;width:79px;height:36px;background:var(--blue)}

/* hero */
.hero{left:0;top:104px;width:977px;height:378px;background:linear-gradient(180deg,#cfd8e2 0,#b9c6d4 38%,#8fa3b4 52%,#7d9a55 72%,#5f7d3a 100%)}
.hero-arrow{top:180px;width:55px;height:53px;background:rgba(255,255,255,.85);display:flex;align-items:center;justify-content:center}
.hero-arrow.prev{left:18px}
.hero-arrow.next{right:12px}
.cta-band{left:0;top:482px;width:977px;height:88px;background:#f2f1ee}
.cta-title{left:57px;top:22px;font-size:30px;color:var(--navy)}
.btn-valuation{left:588px;top:19px;width:327px;height:48px;background:var(--orange);font-size:18px;text-transform:none;font-weight:400}

/* welcome */
.photo-frame{border:1px solid var(--line);padding:10px;background:#fff}
.welcome-photo{left:57px;top:607px;width:209px;height:243px}
.welcome-photo .ph{height:186px;background:linear-gradient(180deg,#9fbf6a 0,#d9dde0 35%,#eceff1 70%,#6e8f40 100%)}
.welcome-photo .cap{color:var(--orange);font-size:13px;font-weight:700;text-align:center;margin-top:16px}
h2{color:var(--orange);font-weight:400}
.welcome{left:282px;top:606px;width:330px}
.welcome h2{font-size:28px;line-height:1.1}
.welcome .sub{color:var(--orange);font-weight:700;font-size:13.5px;margin:6px 0 10px}
.small{font-size:10.5px;line-height:1.7;color:var(--muted)}
.welcome .note{font-size:11px;line-height:1.7;color:var(--text);margin-top:10px}
.services{left:654px;top:606px;width:270px}
.services h2{font-size:28px;line-height:1.1;margin-bottom:18px}
.service{display:flex;align-items:flex-start;margin-bottom:13px}
.service .num{color:var(--blue);font-weight:700;font-size:22px;width:44px;line-height:1}
.service .txt{font-size:11.5px;line-height:1.35;text-transform:uppercase;color:var(--text);padding-top:2px}
.divider{left:0;width:977px;height:1px;background:var(--line)}

/* selling */
.selling-title{left:0;top:912px;width:977px;text-align:center;font-size:29px}
.selling-intro{left:57px;top:960px;width:863px;text-align:center;font-size:12.5px;line-height:1.75;color:var(--muted)}
.card{top:1028px;width:198px;text-align:center}
.card .photo-frame{height:185px;padding:9px}
.card .ph{height:165px}
.card h3{color:var(--orange);font-size:14.5px;margin:20px 0 10px}
.card p{font-size:10.5px;line-height:1.6;color:var(--muted);padding:0 4px}
.btn-more{width:80px;height:37px;background:var(--blue);margin:14px auto 0;font-size:13px;font-weight:700;font-family:inherit}
.btn-more svg{margin-left:8px}

/* testimonials */
.testimonials{left:0;top:1392px;width:977px;height:245px;background:var(--light)}
.testimonials h2{position:absolute;left:0;top:22px;width:977px;text-align:center;font-size:28px;font-weight:700;color:var(--orange)}
.t-arrow{top:32px}
.quote{top:90px;width:400px}
.avatar{width:65px;height:65px;border-radius:50%;border:3px solid #fff;box-shadow:0 0 0 1px #ddd;background:linear-gradient(180deg,#b7c2cc,#7a8794)}
.quote p{position:absolute;left:90px;top:0;width:310px;font-size:10.5px;line-height:1.8;color:var(--muted)}
.quote .by{position:absolute;left:90px;top:78px;font-size:10.5px;color:var(--blue)}
.quote-sep{left:448px;top:90px;width:1px;height:60px;background:#d8d8d8}

/* collection */
.collection{left:0;top:1637px;width:977px;height:269px}
.map-bg{left:80px;top:10px;width:820px;height:250px;background:radial-gradient(ellipse at 50% 50%,#eef1f4 0,#f6f7f8 60%,#fff 100%)}
.collection h2{position:absolute;left:0;top:32px;width:977px;text-align:center;font-size:40px}
.collection .lead{position:absolute;left:0;top:88px;width:977px;text-align:center;font-size:13px;color:var(--muted)}
.location{left:256px;top:121px;width:464px;height:63px;background:#fff;border:1px solid #d8d8d8;border-radius:4px;box-shadow:0 1px 3px rgba(0,0,0,.08)}
.location .flag{left:14px;top:20px}
.location .city{left:42px;top:22px;font-size:13.5px;color:#9a9ea4}
.btn-locations{right:6px;top:6px;height:49px;width:170px;clip-path:polygon(14% 0,100% 0,100% 100%,14% 100%,0 50%);background:var(--blue);font-size:12px;padding-left:20px}
.email{left:0;top:204px;width:977px;text-align:center;font-size:19px;color:var(--blue)}

/* brands */
.brands{left:0;top:1906px;width:977px;height:123px;border-top:1px solid var(--line);display:flex;align-items:center;justify-content:center;gap:14px}
.brand{width:46px;height:30px;border-radius:4px;background:#cfd4da}
.brand.round{border-radius:50%;width:44px;height:44px;background:#8b2a2a}
.brand.red{background:#d9382e}
.brand.blue{background:#2f5f9e}
.brand.green{background:#3b6b45}
.brand.orange{background:#e8922a}

/* footer */
.footer{left:104px;top:2101px;width:996px;height:75px;background:var(--navy)}
.social{top:22px;width:32px;height:32px;border-radius:50%;border:1.5px solid #8a93a0}
.social.active{border-color:var(--orange)}
.copyright{right:60px;top:29px;font-size:10.5px;color:#8a93a0}
</style>
</head>
<body>
<div class="city-backdrop" role="img" aria-label="Dusky city skyline behind the page"></div>
<div class="page-shadow"></div>

<div class="page">
  <!-- header -->
  <div class="abs logo">
    <div class="logo-name">trailquote.example</div>
    <div class="logo-tag">The UK's largest buyer of touring caravans</div>
  </div>
  <nav class="abs nav">
    <a class="active" href="#">Home</a><a href="#">How it Works</a><a href="#">FAQ's</a><a href="#">Contact us</a>
  </nav>
  <div class="abs btn btn-join"><svg width="14" height="14" viewBox="0 0 14 14" style="margin-right:6px"><path d="M7 1v12M1 7h12" stroke="#fff" stroke-width="3"/></svg>Join us</div>
  <div class="abs btn btn-login">Log in</div>

  <!-- hero -->
  <div class="abs hero" role="img" aria-label="Touring caravan with awning parked on grass beside a lake">
    <div class="abs hero-arrow prev"><svg width="16" height="22" viewBox="0 0 16 22"><path d="M13 2 4 11l9 9" stroke="#9aa3ad" stroke-width="4" fill="none"/></svg></div>
    <div class="abs hero-arrow next"><svg width="16" height="22" viewBox="0 0 16 22"><path d="M3 2l9 9-9 9" stroke="#9aa3ad" stroke-width="4" fill="none"/></svg></div>
  </div>
  <div class="abs cta-band">
    <div class="abs cta-title">Sell your caravan quickly and securely</div>
    <div class="abs btn btn-valuation">Request a FREE Caravan Valuation</div>
  </div>

  <!-- welcome -->
  <div class="abs photo-frame welcome-photo">
    <div class="ph" role="img" aria-label="White motorhome parked on a grassy field"></div>
    <div class="cap">Sunt in culpa qui officia</div>
  </div>
  <div class="abs welcome">
    <h2>Welcome to trailquote</h2>
    <div class="sub">The UK's largest buyer of touring caravans</div>
    <p class="small">Selling your caravan to trailquote.example saves you the usual headaches and costs associated with selling a caravan, not to mention the potential risks involved. All you need to do is either call us on the freephone number provided, or click the button above and complete our online requ........</p>
    <p class="note">Remember, there are no hidden charges for our service and you are not under any obligation to accept our offer. You really do have nothing to lose by simply finding out how much we can pay for your caravan.</p>
  </div>
  <div class="abs services">
    <h2>Our other services</h2>
    <div class="service"><span class="num">01</span><span class="txt">Genuine online or verbal offer to purchase</span></div>
    <div class="service"><span class="num">02</span><span class="txt">Excellent prices offered and paid</span></div>
    <div class="service"><span class="num">03</span><span class="txt">No admin fees or hidden charges</span></div>
    <div class="service"><span class="num">04</span><span class="txt">Friendly professional, no hassle service</span></div>
    <div class="service"><span class="num">05</span><span class="txt">Instant cash or faster payment bank transfer</span></div>
  </div>
  <div class="abs divider" style="top:891px"></div>

  <!-- selling -->
  <h2 class="abs selling-title">Selling your Campervan?</h2>
  <p class="abs selling-intro">Selling your caravan to trailquote.example saves you the usual headaches and costs associated with selling a caravan, not to mention the potential risks involved. All you need to do is either call us on the freephone number provided, or click the button above and complete our online requ........</p>

  <div class="abs card" style="left:57px">
    <div class="photo-frame"><div class="ph" role="img" aria-label="Static caravan under a blue sky" style="background:linear-gradient(180deg,#6d9ad0 0,#b9cfe6 40%,#e6e9ec 65%,#7ea04a 100%)"></div></div>
    <h3>Lorem ipsum dolor sit amet</h3>
    <p>Selling your caravan to trailquote.example saves you the usual headaches and costs associated with selling a caravan.</p>
    <div class="btn btn-more">More<svg width="7" height="10" viewBox="0 0 7 10"><path d="M1 1l4 4-4 4" stroke="#fff" stroke-width="2" fill="none"/></svg></div>
  </div>
  <div class="abs card" style="left:278px">
    <div class="photo-frame"><div class="ph" role="img" aria-label="Caravan parked on a sunny beach" style="background:linear-gradient(180deg,#2f6fb8 0,#6fa6d8 45%,#d9d2a6 70%,#b4a75e 100%)"></div></div>
    <h3>Lorem ipsum dolor sit amet</h3>
    <p>Selling your caravan to trailquote.example saves you the usual headaches and costs associated with selling a caravan.</p>
    <div class="btn btn-more">More<svg width="7" height="10" viewBox="0 0 7 10"><path d="M1 1l4 4-4 4" stroke="#fff" stroke-width="2" fill="none"/></svg></div>
  </div>
  <div class="abs card" style="left:499px">
    <div class="photo-frame"><div class="ph" role="img" aria-label="Caravan parked among green trees" style="background:linear-gradient(180deg,#3f7a2c 0,#8fb95a 40%,#dfe3e0 60%,#5b8f2f 100%)"></div></div>
    <h3>Lorem ipsum dolor sit amet</h3>
    <p>Selling your caravan to trailquote.example saves you the usual headaches and costs associated with selling a caravan.</p>
    <div class="btn btn-more">More<svg width="7" height="10" viewBox="0 0 7 10"><path d="M1 1l4 4-4 4" stroke="#fff" stroke-width="2" fill="none"/></svg></div>
  </div>
  <div class="abs card" style="left:720px">
    <div class="photo-frame"><div class="ph" role="img" aria-label="Caravan with blue awning on a campsite" style="background:linear-gradient(180deg,#5a8fd0 0,#a9c6e6 35%,#5c6f94 60%,#6b9a3e 100%)"></div></div>
    <h3>Lorem ipsum dolor sit amet</h3>
    <p>Selling your caravan to trailquote.example saves you the usual headaches and costs associated with selling a caravan.</p>
    <div class="btn btn-more">More<svg width="7" height="10" viewBox="0 0 7 10"><path d="M1 1l4 4-4 4" stroke="#fff" stroke-width="2" fill="none"/></svg></div>
  </div>

  <!-- testimonials -->
  <section class="abs testimonials">
    <div class="abs" style="left:0;top:0;width:977px;height:1px;background:var(--line)"></div>
    <h2>What Our Client Says</h2>
    <svg class="abs t-arrow" style="left:330px" width="14" height="20" viewBox="0 0 14 20"><path d="M11 2 3 10l8 8" stroke="#b5b9be" stroke-width="4" fill="none"/></svg>
    <svg class="abs t-arrow" style="left:633px" width="14" height="20" viewBox="0 0 14 20"><path d="M3 2l8 8-8 8" stroke="#9aa0a7" stroke-width="4" fill="none"/></svg>
    <div class="abs quote" style="left:57px">
      <div class="avatar" role="img" aria-label="Client portrait"></div>
      <p>Lorem ipsum dolor sit amet, consectetur adipisicing elit, sed do eiusmod tempor incididunt ut labore et dolore magna aliqua. Ut enim ad minim veniam, quis nostrud exercitation ullamco laboris nisi</p>
      <div class="by">Tobias Marrow, CEO of B2B agency Veldcrest</div>
    </div>
    <div class="abs quote-sep"></div>
    <div class="abs quote" style="left:505px">
      <div class="avatar" role="img" aria-label="Client portrait"></div>
      <p>Lorem ipsum dolor sit amet, consectetur adipisicing elit, sed do eiusmod tempor incididunt ut labore et dolore magna aliqua. Ut enim ad minim veniam, quis nostrud exercitation ullamco laboris nisi</p>
      <div class="by">Tobias Marrow, CEO of B2B agency Veldcrest</div>
    </div>
  </section>

  <!-- collection -->
  <section class="abs collection">
    <div class="abs map-bg" role="img" aria-label="Faint world map behind the collection area"></div>
    <h2>Free Collection</h2>
    <div class="lead">Below are some examples of of the areas we cover ...</div>
    <div class="abs location">
      <svg class="abs flag" width="16" height="22" viewBox="0 0 16 22"><path d="M8 1c-4 0-7 3-7 7 0 5 7 13 7 13s7-8 7-13c0-4-3-7-7-7z" fill="#c8313b"/><circle cx="8" cy="8" r="3" fill="#fff"/></svg>
      <div class="abs city">Birmingham</div>
      <div class="abs btn btn-locations">View all locations<svg width="9" height="6" viewBox="0 0 9 6" style="margin-left:5px"><path d="M0 0h9L4.5 6z" fill="#fff"/></svg></div>
    </div>
    <div class="abs email">info@trailquote.example</div>
  </section>

  <!-- brands -->
  <div class="abs brands">
    <svg width="12" height="18" viewBox="0 0 12 18" style="margin-right:6px"><path d="M10 2 3 9l7 7" stroke="#c9cdd2" stroke-width="3" fill="none"/></svg>
    <div class="brand red" style="height:10px"></div>
    <div class="brand green" style="width:32px;height:40px"></div>
    <div class="brand blue" style="border-radius:50%;height:28px"></div>
    <div class="brand blue" style="width:32px;height:40px"></div>
    <div class="brand red" style="height:16px"></div>
    <div class="brand green" style="width:32px;height:38px;background:#2a8f7a"></div>
    <div class="brand" style="height:18px"></div>
    <div class="brand orange" style="width:40px;height:40px"></div>
    <div class="brand" style="height:16px;background:#6a7a9a"></div>
    <div class="brand orange" style="width:36px;height:36px"></div>
    <div class="brand red" style="border-radius:50%;height:24px"></div>
    <div class="brand red" style="width:36px;height:40px"></div>
    <div class="brand red" style="height:18px"></div>
    <div class="brand blue" style="width:34px;height:40px"></div>
    <div class="brand round"></div>
    <svg width="12" height="18" viewBox="0 0 12 18" style="margin-left:6px"><path d="M2 2l7 7-7 7" stroke="#9aa0a7" stroke-width="3" fill="none"/></svg>
  </div>
</div>

<!-- footer -->
<footer class="abs footer">
  <div class="abs social" style="left:67px"></div>
  <div class="abs social active" style="left:108px"></div>
  <div class="abs social" style="left:149px"></div>
  <div class="abs social" style="left:190px"></div>
  <div class="abs copyright">© 2014 - Trailquote.example - Elm Row - Brackford - Kent ZZ1 2AB All rights reserved.</div>
</footer>
</body>
</html>
```